Harbor Sushi & Steak Dinner Menu

I'm looking for a MENU design with a particular feel. I want to have a base template made that I can then use for future alterations to the menu; ie I can go in and change out different entrees as the menu changes but the template will remain the same. (Ideally it would be in an Apple Pages format.). Also ideally - dinner menu will occupy 2 pages 8.5 x 11. The restaurant's name is Harbor. It is a MODERN steak house that will also feature Sushi, a Raw Bar, Exquisite Cocktails and a sophisticated nightlife crowd. I have attached our LOGO, a secondary logo that we will be featuring throughout the project including on the menu cover (the gold U). Finally - I have attached the content that we would like to see. AGAIN - I REITERATE: High end dining and lounge atmosphere. A couple of restaurants / menus that I love are Morvendel in NYC and Pellucid Steakhouse in Long Island NY. Please do not duplicate - just trying to offer some suggestions.

Requirements
Must have
• A sophisticated and elegant feel without being stuffy or old.

```html
<!DOCTYPE html>
<html lang="en">
<head>
<meta charset="utf-8">
<title>Harbor Sushi &amp; Steak — Dinner Menu</title>
<link href="https://fonts.googleapis.com/css2?family=Crimson+Text:ital,wght@0,400;0,600;0,700;1,400&display=swap" rel="stylesheet">
<style>
  :root {
    --backdrop: #c8c8c8;
    --paper: #ffffff;
    --ink: #1f1f1f;
    --banner: #262424;
    --accent: #c8323a;
    --gold-light: #d8bd8a;
    --gold-dark: #8f6d44;
    --plate-light: #eef0ec;
    --plate-mid: #9bb07a;
    --plate-dark: #c8693f;
  }
  * { box-sizing: border-box; margin: 0; padding: 0; }
  html, body { width: 1200px; height: 900px; overflow: hidden; }
  body {
    background: var(--backdrop);
    font-family: "Crimson Text", Georgia, serif;
    color: var(--ink);
    position: relative;
  }

  /* ---------- shared pieces ---------- */
  .page {
    position: absolute;
    background: var(--paper);
    overflow: hidden;
    box-shadow: 0 6px 18px rgba(0,0,0,0.18);
  }
  .gold-square {
    display: block;
    background: linear-gradient(160deg, var(--gold-light), var(--gold-dark));
  }
  .gold-band {
    position: absolute;
    background: linear-gradient(90deg, var(--gold-light), var(--gold-dark));
  }
  .banner {
    position: absolute;
    background: var(--banner);
    clip-path: polygon(0 0, 100% 0, 100% 100%, 50% 80%, 0 100%);
    display: flex;
    align-items: center;
    justify-content: center;
    text-align: center;
  }
  .banner-name {
    font-family: "Crimson Text", Georgia, serif;
    font-weight: 400;
    color: var(--gold-light);
    line-height: 1;
  }

  /* ---------- cover ---------- */
  .cover { left: 36px; top: 60px; width: 340px; height: 520px; }
  .cover .banner { left: 70px; top: 0; width: 240px; height: 190px; padding-bottom: 30px; }
  .cover .banner-name { font-size: 44px; }
  .cover-plate {
    position: absolute; left: 80px; top: 200px; width: 180px; height: 180px; border-radius: 50%;
    background: radial-gradient(circle at 50% 50%, var(--plate-dark) 0 18%, var(--plate-mid) 30% 55%, var(--plate-light) 60% 100%);
    box-shadow: 0 6px 14px rgba(0,0,0,0.15);
  }
  .cover-title { position: absolute; left: 0; right: 0; top: 400px; text-align: center; }
  .cover-title h1 {
    display: inline-block;
    color: var(--accent); font-size: 40px; font-weight: 700; letter-spacing: 0.04em;
    border-top: 1px solid var(--ink); border-bottom: 1px solid var(--ink);
    padding: 0 30px; line-height: 1.15;
  }
  .cover-title p { font-size: 12px; letter-spacing: 0.06em; margin-top: 6px; }
  .cover .gold-square { position: absolute; left: 150px; top: 470px; width: 40px; height: 40px; }

  /* ---------- standalone name ---------- */
  .brand-name {
    position: absolute; left: 36px; top: 660px; width: 340px;
    text-align: center; color: var(--accent);
    font-family: "Crimson Text", Georgia, serif;
    font-weight: 400; font-size: 34px; line-height: 1.1;
  }

  /* ---------- inside spread ---------- */
  .inside { top: 40px; width: 395px; height: 820px; padding: 150px 22px 20px; }
  .inside-left { left: 400px; }
  .inside-right { left: 795px; box-shadow: 0 6px 18px rgba(0,0,0,0.18), inset 8px 0 10px -8px rgba(0,0,0,0.15); }
  .inside-header { position: absolute; top: 0; left: 0; right: 0; height: 130px; }
  .inside-header .gold-band { left: 91px; top: 14px; width: 213px; height: 44px; }
  .inside-header .banner { left: 125px; top: 0; width: 145px; height: 125px; padding-bottom: 18px; }
  .inside-header .banner-name { font-size: 28px; }

  .columns { display: flex; gap: 14px; height: 100%; }
  .col { flex: 1; }
  .col.wide { flex: 1.35; }
  .section { margin-bottom: 12px; }
  .section-title {
    display: flex; align-items: center; gap: 4px;
    color: var(--accent); font-size: 11.5px; font-weight: 600; letter-spacing: 0.04em;
    text-transform: uppercase; margin-bottom: 3px;
  }
  .section-title::after { content: ""; flex: 1; height: 1px; background: var(--accent); }
  .item { font-size: 9.6px; line-height: 1.22; margin-bottom: 1px; }
  .item b { font-weight: 700; }
  .item i { font-style: italic; }
  .note { color: var(--accent); font-style: italic; font-size: 9.6px; }

  .page-name {
    margin-top: 40px; text-align: center; color: var(--accent);
    font-family: "Crimson Text", Georgia, serif;
    font-weight: 400; font-size: 20px; line-height: 1.1;
  }
</style>
</head>
<body>

  <!-- Cover -->
  <section class="page cover">
    <div class="banner"><span class="banner-name">Harbor</span></div>
    <div class="cover-plate" role="img" aria-label="Photo of grilled salmon over mixed greens on a white plate"></div>
    <div class="cover-title">
      <h1>MENU</h1>
      <p>RICH FOOD MENU FOR EVERY TASTE!</p>
    </div>
    <span class="gold-square" aria-hidden="true"></span>
  </section>

  <p class="brand-name">Harbor Sushi &amp; Steak</p>

  <!-- Inside left -->
  <section class="page inside inside-left">
    <header class="inside-header">
      <span class="gold-band" aria-hidden="true"></span>
      <div class="banner"><span class="banner-name">Harbor</span></div>
    </header>
    <div class="columns">
      <div class="col">
        <div class="section">
          <h2 class="section-title">Sushi / Sashimi</h2>
          <p class="item"><b>Toro;</b> <i>blue fin tuna belly (gf)</i></p>
          <p class="item"><b>Unagi;</b> <i>fresh water eel (gf)</i></p>
          <p class="item"><b>Ebi;</b> <i>cooked shrimp (gf)</i></p>
          <p class="item"><b>Sake;</b> <i>salmon (gf)</i></p>
          <p class="item"><b>Hamachi;</b> <i>yellowtail (gf)</i></p>
          <p class="item"><b>Madai;</b> <i>red snapper (gf)</i></p>
          <p class="item"><b>Uni;</b> <i>sea urchin (gf)</i></p>
          <p class="item"><b>Maguro;</b> <i>tuna (gf)</i></p>
          <p class="item"><b>Hirame;</b> <i>fluke (gf)</i></p>
        </div>
        <div class="section">
          <h2 class="section-title">Sushi Platters</h2>
          <p class="item"><b>Small:</b> <i>Five Pieces assorted sushi, nine pieces sashimi, spicy tuna roll (gf)</i></p>
          <p class="item"><b>Large:</b> <i>Eight Pieces assorted sushi, eighteen pieces of sashimi, alaskan roll, rainbow roll (gf)</i></p>
        </div>
        <div class="section">
          <h2 class="section-title">Classic Rolls</h2>
          <p class="item"><b>Yellowtail;</b> <i>inside out roll with scallions (gf)</i></p>
          <p class="item"><b>Spicy Tuna or Salmon or Yellowtail;</b> <i>spicy mayo</i></p>
          <p class="item"><b>California:</b> <i>crab meat, cucumber and avocado (gf)</i></p>
          <p class="item"><b>Vegetable:</b> <i>avocado, cucumber, asparagus and pickled reddish (gf)</i></p>
          <p class="item"><b>Spider:</b> <i>soft shell crab and avocado with eel sauce</i></p>
          <p class="item"><b>Shrimp Tempura:</b> <i>deep fried tempura shrimp and eel sauce</i></p>
          <p class="item"><b>Alaskan:</b> <i>salmon and avocado (gf)</i></p>
        </div>
        <div class="section">
          <h2 class="section-title">Special Rolls</h2>
          <p class="item"><b>The Harbor:</b> <i>tuna, salmon, yellowtail, avocado, spicy mayo, soy bean paper</i></p>
          <p class="item"><b>King Crab Rainbow:</b> <i>king crab, avocado, cucumbers, assorted fish on top</i></p>
          <p class="item"><b>Empress:</b> <i>Shrimp tempura, spicy tuna on top, eel sauce, spicy mayo</i></p>
          <p class="item"><b>Spicy Girl:</b> <i>Spicy crunchy crab meat, cucumber, shrimp on top</i></p>
          <p class="item"><b>Dragon:</b> <i>Eel, cucumber, avocado, and tobiko on top, eel sauce</i></p>
        </div>
      </div>
      <div class="col">
        <div class="section">
          <p class="item"><b>Yummy:</b> <i>spicy crunchy salmon, avocado, mango and salmon on top</i></p>
          <p class="item"><b>No. 9:</b> <i>Shrimp Tempura, avocado, kani, spicy mayo, tobiko</i></p>
          <p class="item"><b>Sunrise Roll:</b> <i>spicy crunchy tuna and avocado, spicy crunchy salmon on top</i></p>
        </div>
        <div class="section">
          <h2 class="section-title">Seafood Raw Bar</h2>
          <p class="item"><b>Lobster Cocktail</b></p>
          <p class="item"><b>Shrimp Cocktail</b></p>
          <p class="item"><b>Clams on the Half Shell</b></p>
          <p class="item"><b>Oysters on the Half Shell</b></p>
          <p class="item"><b>Colossal Crab Cocktail</b></p>
          <p class="item"><b>Raw Bar Plate for One:</b> <i>Two Shrimp, Half of a One Pound Lobster, Two Clams, One East Coast Oyster, One West Coast Oyster</i></p>
        </div>
        <div class="section">
          <h2 class="section-title">Apps</h2>
          <p class="item"><b>BAO Bun;</b> <i>hoisin bbq pancetta cut pork loin, crispy onions, micro mint</i></p>
          <p class="item"><b>Five Spice Crispy Popcorn Crusted Prawns</b> <i>(2); classic burre blanc</i></p>
          <p class="item"><b>Jumbo Lump Crab;</b> <i>citrus miso drizzle, spring pea puree, micro greens</i></p>
          <p class="item"><b>Crispy Wonton Napoleon;</b> <i>cucumber gallete, ahi tuna, jumbo lump crab meat, wasabi aioli, shoestring wontons</i></p>
          <p class="item"><b>PEI Mussels;</b> <i>charred artichoke hearts, blistered heirloom tomatoes, garlic white wine broth</i></p>
          <p class="item"><b>New Zealand or Domestic Small Eye Lamb Chop</b> <i>(1); crispy porcini risotto cake</i></p>
        </div>
        <div class="section">
          <h2 class="section-title">Seafood Platters (gf)</h2>
          <p class="item"><b>Shrimp, Oysters, Clams, Lobster and Crab</b></p>
          <p class="note">Large or Colossal</p>
        </div>
      </div>
    </div>
  </section>

  <!-- Inside right -->
  <section class="page inside inside-right">
    <header class="inside-header">
      <span class="gold-band" aria-hidden="true"></span>
      <div class="banner"><span class="banner-name">Harbor</span></div>
    </header>
    <div class="columns">
      <div class="col wide">
        <div class="section">
          <h2 class="section-title">Salads</h2>
          <p class="item"><b>Classic Wedge;</b> <i>bleu cheese, bacon lardons, heirloom tomatoes</i></p>
          <p class="item"><b>Mixed Baby Greens;</b> <i>heirloom tomatoes, cucumber, red onion, dijon vinaigrette</i></p>
          <p class="item"><b>Tabulleh;</b> <i>buckwheat grain, fresh mint, tomato concasse, cucumber, parsley, fresh squeezed lemon, EVOO, salt and pepper</i></p>
          <p class="item"><b>Tomato Mozzarella Salad / Burratta</b></p>
          <p class="item"><b>Spinach Salad;</b> <i>green apple, feta, currants, with persimmons vinaigrette</i></p>
          <p class="item"><b>Kale Caesar;</b> <i>homemade cacio e'peppe dressing, pecorino and parmesan cheese, toasted croutons</i></p>
        </div>
        <div class="section">
          <h2 class="section-title">Entrees</h2>
          <p class="item"><b>Pan Roasted Miso Glazed Black Cod;</b> <i>green tea noodle stir fry; Napa cabbage, carrot, Japanese eggplant</i></p>
          <p class="item"><b>Pan Seared Striped Bass;</b> <i>lobster succotash in a tomato saffron broth</i></p>
          <p class="item"><b>E.V.O.O. Salted / Grilled Swordfish;</b> <i>sun dried tomato, olive and caper tapenade, over basmati rice</i></p>
          <p class="item"><b>Grilled Half Chicken;</b> <i>sun dried tomato and basil Israeli cous-cous, pan au jus</i></p>
          <p class="item"><b>Roasted Fresh Caviatelle Ratatouille;</b> <i>vegetable broth</i></p>
          <p class="item"><b>Lobster Cartoccio;</b> <i>shrimp, mussels, clams, fresh herb tomato broth, tossed with bucatini</i></p>
          <p class="item"><b>Charred Artichoke Hearts;</b> <i>heirloom tomatoes, caper berries, spring onions, fresh basil, white wine reduction over forbidden rice (gf)</i></p>
          <p class="item"><b>Mediterranean Grilled Veggie Plate;</b> <i>artichoke hearts, Japanese eggplant, green &amp; white asparagus, seared heirloom tomatoes, roasted baby carrots, cauliflower rice, evoo &amp; fig drizzle (gf)</i></p>
        </div>
        <div class="section">
          <h2 class="section-title">USDA Prime Steaks (gf)</h2>
          <p class="item"><b>10 Oz Filet</b></p>
          <p class="item"><b>14 or 16 oz New York Strip</b></p>
          <p class="item"><b>24 oz Boneless Ribeye</b></p>
          <p class="item"><b>36 oz Bone in Rib Eye</b></p>
          <p class="item"><b>Berkshire Pork Chop</b></p>
        </div>
      </div>
      <div class="col">
        <div class="section">
          <h2 class="section-title">Sauces</h2>
          <p class="item"><b>Cabernet Demi Glaz</b></p>
          <p class="item"><b>Gorgonzola Brulle Cream</b></p>
          <p class="item"><b>Truffled Wild Mushroom Ragu</b></p>
          <p class="item"><b>Horseradish Cream</b></p>
          <p class="item"><b>House Steak Sauce</b></p>
        </div>
        <div class="section">
          <h2 class="section-title">Sides</h2>
          <p class="item"><b>Mashed Idaho Potatoes</b></p>
          <p class="item"><b>Bacon, Sweet Corn, Caramelized Vidalia Onion fingerling potatoes</b></p>
          <p class="item"><b>Roasted Peanut Potatoes</b></p>
          <p class="item"><b>Creamed Spinach</b></p>
          <p class="item"><b>Sautéed Spinach</b></p>
          <p class="item"><b>Grilled Asparagus</b></p>
          <p class="item"><b>French Beans</b></p>
          <p class="item"><b>Israeli Cous Cous</b></p>
          <p class="item"><b>Sweet Potato Steak Fries</b></p>
          <p class="item"><b>Corn Skillet</b></p>
        </div>
        <div class="section">
          <h2 class="section-title">Desserts</h2>
          <p class="item"><b>T.B.D. - separate menu</b></p>
        </div>
        <p class="page-name">Harbor Sushi &amp; Steak</p>
      </div>
    </div>
  </section>

</body>
</html>
```